Copper Ridge Resort & Marina - Boat Slips, Cabin Rentals, Floating Vacation Homes, & More

We need an 8'H x 16'W billboard for our Resort & marina, www.copperridgeresort.example. We'd like it to include: Lakefront Cabin Rentals, Floating Vacation Homes, and New Slips Summer 2022. We'd like it to be simple using the colors on our logo, similar to our business cards, and have our logo on it large. Maybe an arrow on the bottom pointing left that says 3 miles, possibly our website and phone number.

Target Market(s)

Lake People, Boaters

Industry/Entity Type

Resort & Marina (Recreation/Hospitality)

Font styles to use
Sans Serif
Other font styles liked:
• Simple/modern

Colors
0054AA
0677BA
7BADD7
CADEEF
E8F1F8
FFC000
F8CF3A
FAE287
FDF2CF
FEFAEE
F0912C
F2A743
F7CA91
FBE8D2
FDF5EE

Requirements
Must have
• Logo, Cabin Rentals, Floating Vacation Homes, New Slips Summer 2022
Nice to have
• An additional banner hanging from the bottom with an orange (or blue, colors from our logo) arrow pointing left, with white text saying: 3 miles 555-214-0867 www.copperridgeresort.example
Should not have
• Shouldn't be too busy

```html
<!DOCTYPE html>
<html lang="en">
<head>
<meta charset="utf-8">
<title>Copper Ridge Resort &amp; Marina — Billboard</title>
<link rel="stylesheet" href="https://fonts.googleapis.com/css2?family=Montserrat:wght@700;800;900&display=swap">
<style>
  :root {
    --blue-deep: #0054AA;
    --blue-navy: #134a85;
    --blue-mid: #0677BA;
    --blue-pale: #E8F1F8;
    --gold: #F8A61E;
    --gold-bright: #FFC000;
    --orange: #F0912C;
    --ink: #151515;
    --paper: #ffffff;
    --backdrop: #e9eef3;
  }
  * { margin: 0; padding: 0; box-sizing: border-box; }
  html, body { width: 1200px; height: 1200px; overflow: hidden; }
  body {
    background: var(--backdrop);
    font-family: "Montserrat", sans-serif;
    display: flex; align-items: center; justify-content: center;
  }
  .billboard {
    position: relative;
    width: 1200px; height: 600px;
    background: linear-gradient(135deg, var(--paper) 0%, #f6f7f9 60%, var(--paper) 100%);
    overflow: hidden;
  }
  .brand {
    position: absolute; left: 60px; top: 46px;
    display: flex; align-items: center; gap: 22px;
  }
  .brand-mark {
    width: 86px; height: 86px; border-radius: 50%;
    background: var(--orange);
  }
  .brand-name {
    color: var(--blue-navy);
    font-weight: 800; font-size: 46px; line-height: 1.05;
    letter-spacing: 0.02em;
  }
  .offer-list {
    position: absolute; left: 100px; top: 196px;
    list-style: none;
  }
  .offer-list li {
    display: flex; align-items: center; gap: 18px;
    font-weight: 900; font-size: 40px; color: var(--ink);
    letter-spacing: 0.02em; line-height: 1.35;
    text-transform: uppercase; white-space: nowrap;
  }
  .offer-list svg { width: 36px; height: 36px; flex: none; }
  .lake-map {
    position: absolute; right: 40px; top: 40px;
    width: 330px; height: 330px;
    background: radial-gradient(ellipse at 55% 50%, #3a6eae 0%, var(--blue-navy) 45%, rgba(19,74,133,0.08) 72%, transparent 80%);
  }
  .distance-band, .contact-band { position: absolute; }
  .distance-band { left: 0; top: 420px; width: 470px; height: 120px; }
  .distance-label {
    position: absolute; left: 70px; top: 420px; height: 120px;
    display: flex; align-items: center;
    color: var(--paper); font-weight: 900; font-size: 76px; letter-spacing: 0.01em;
    white-space: nowrap;
  }
  .contact-band { left: 400px; top: 420px; width: 800px; height: 180px; }
  .contact {
    position: absolute; left: 500px; top: 420px; width: 670px;
    white-space: nowrap;
  }
  .contact-phone {
    color: var(--paper); font-weight: 900; font-size: 88px; line-height: 1.25; letter-spacing: 0.01em;
  }
  .contact-web {
    color: var(--gold-bright); font-weight: 800; font-size: 28px;
    text-transform: uppercase; letter-spacing: 0; margin-top: 4px;
  }
</style>
</head>
<body>
  <main class="billboard">
    <header class="brand">
      <span class="brand-mark"></span>
      <span class="brand-name">COPPER RIDGE<br>RESORT &amp; MARINA</span>
    </header>

    <ul class="offer-list">
      <li>
        <svg viewBox="0 0 36 36" aria-hidden="true"><circle cx="18" cy="18" r="14" fill="none" stroke="var(--blue-navy)" stroke-width="4"/><path d="M10 17l7 7 13-15" fill="none" stroke="var(--gold)" stroke-width="5" stroke-linecap="round" stroke-linejoin="round"/></svg>
        Cabin Rentals
      </li>
      <li>
        <svg viewBox="0 0 36 36" aria-hidden="true"><circle cx="18" cy="18" r="14" fill="none" stroke="var(--blue-navy)" stroke-width="4"/><path d="M10 17l7 7 13-15" fill="none" stroke="var(--gold)" stroke-width="5" stroke-linecap="round" stroke-linejoin="round"/></svg>
        Floating Vacation Homes
      </li>
      <li>
        <svg viewBox="0 0 36 36" aria-hidden="true"><circle cx="18" cy="18" r="14" fill="none" stroke="var(--blue-navy)" stroke-width="4"/><path d="M10 17l7 7 13-15" fill="none" stroke="var(--gold)" stroke-width="5" stroke-linecap="round" stroke-linejoin="round"/></svg>
        New Slips Summer 2022
      </li>
    </ul>

    <div class="lake-map" role="img" aria-label="Map of Lake Harlow with the resort location marked"></div>

    <svg class="distance-band" viewBox="0 0 470 120" aria-hidden="true">
      <polygon points="0,60 40,0 470,0 430,60 470,120 40,120" fill="var(--gold)"/>
    </svg>
    <div class="distance-label">3 MILES</div>

    <svg class="contact-band" viewBox="0 0 800 180" aria-hidden="true">
      <polygon points="0,60 60,0 800,0 800,180 60,180 60,120" fill="var(--blue-navy)"/>
    </svg>
    <div class="contact">
      <p class="contact-phone">555-214-0867</p>
      <p class="contact-web">www.copperridgeresort.example</p>
    </div>
  </main>
</body>
</html>
```